business card for training & coaching company, Brightwell.co

Create a warm, clean, professional 2-sided business card for Brightwell.co.
Brightwell.co is a new company that shares Brightwell Dialogue (combination of mindfulness, kindness, and nonviolent communication), training and coaching individuals and groups.
Include the logo provided, perhaps incorporating a second opaque version of it as well.
Feelings & Needs lists on the reverse side of the card.

Target Market(s)

Women 30-60 years old, university educated.
Spiritual, may be Buddhist.

Industry/Entity Type

Training

Contact Information for Business Card

Marisabel T. Oberholt, MSc
Group Facilitator & Certified Wellness Coach
Brightwell Dialogue training & support
Group Facilitator & Coach
01632 960 418
07700 900 862
www.brightwell-example.co

Font styles to use
Sans Serif

Requirements
Must have
• Front -- Contact details, logo provided.
• Back -- Feelings list; Needs list
• Professional yet warm, inviting, friendly feel.
Nice to have
• little graphics (telephone for phone number, envelope for email, globe for web);
• Clean font (like Sathu, Frutiga, Helvetica).
• Feeling of movement or transformation.
Should not have
• More than 3 colours.
• Loud or busy designs.
• A gentle curve or two is ok, but not swirly designs.
• No black or other heavy backgrounds.

```html
<!DOCTYPE html>
<html lang="en">
<head>
<meta charset="utf-8">
<title>Brightwell.co business card</title>
<link rel="stylesheet" href="https://fonts.googleapis.com/css2?family=Mulish:wght@400;700&display=swap">
<style>
  :root {
    --orange: #f07a1e;
    --orange-deep: #ec6a1c;
    --orange-faint: #fbe3cf;
    --card: #ffffff;
    --backdrop: #e9e6e2;
  }
  * { box-sizing: border-box; margin: 0; padding: 0; }
  html, body { width: 1200px; height: 1000px; overflow: hidden; }
  body {
    background: var(--backdrop);
    font-family: "Mulish", "Helvetica Neue", Arial, sans-serif;
    color: var(--orange);
    position: relative;
  }
  .card {
    position: absolute;
    background: var(--card);
    border-radius: 26px;
    overflow: hidden;
  }
  .card-front { left: 50px; top: 168px; width: 395px; height: 664px; }
  .card-back { left: 493px; top: 301px; width: 662px; height: 396px; }

  .brand-mark {
    position: absolute; left: 52px; top: 60px;
    width: 200px; height: 200px; border-radius: 50%;
    background: linear-gradient(160deg, #f7961f, var(--orange-deep));
  }
  .brand-name {
    position: absolute; left: 44px; top: 270px;
    font-size: 38px; font-weight: 700; color: var(--orange);
    letter-spacing: 0.2px;
  }
  .holder-name {
    position: absolute; left: 38px; top: 390px;
    font-size: 19px; font-weight: 700;
  }
  .contact-list { position: absolute; left: 38px; top: 436px; list-style: none; }
  .contact-list li {
    display: flex; align-items: center; gap: 4px;
    font-size: 20px; line-height: 26.5px;
  }
  .contact-list svg { width: 15px; height: 15px; flex: none; }
  .role-lines {
    position: absolute; left: 38px; top: 530px;
    font-size: 17.5px; line-height: 22.7px;
  }

  .back-mark {
    position: absolute; left: 160px; top: 50px;
    width: 340px; height: 340px; border-radius: 50%;
    background: var(--orange-faint); opacity: 0.7;
  }
  .list-block {
    position: absolute; left: 0; width: 100%;
    text-align: center; font-size: 18px; line-height: 25px;
  }
  .list-block h2 { font-size: 19px; font-weight: 700; line-height: 25px; }
  .needs { top: 68px; }
  .feelings { top: 225px; }
</style>
</head>
<body>
  <section class="card card-front">
    <div class="brand-mark" aria-hidden="true"></div>
    <div class="brand-name">Brightwell.co</div>
    <div class="holder-name">Marisabel T. Oberholt</div>
    <ul class="contact-list">
      <li><svg viewBox="0 0 16 16" aria-hidden="true"><path d="M4 2 C2 4 2 8 5 11 C8 14 12 14 14 12 L11.5 9.5 L10 11 C8 10 6 8 5 6 L6.5 4.5 Z" fill="var(--orange)"/></svg>01632 960 418</li>
      <li><svg viewBox="0 0 16 16" aria-hidden="true"><path d="M4 2 C2 4 2 8 5 11 C8 14 12 14 14 12 L11.5 9.5 L10 11 C8 10 6 8 5 6 L6.5 4.5 Z" fill="var(--orange)"/></svg>07700 900 862</li>
      <li><svg viewBox="0 0 16 16" aria-hidden="true"><g fill="none" stroke="var(--orange)" stroke-width="1.2"><circle cx="8" cy="8" r="6.5"/><ellipse cx="8" cy="8" rx="3" ry="6.5"/><path d="M1.5 8 H14.5 M2.5 4.8 H13.5 M2.5 11.2 H13.5"/></g></svg>www.brightwell-example.co</li>
    </ul>
    <p class="role-lines">MSc Group Facilitator &amp; Certified<br>Wellness Coach Brightwell<br>Dialogue training &amp; support<br>Group Facilitator &amp; Coach</p>
  </section>

  <section class="card card-back">
    <div class="back-mark" aria-hidden="true"></div>
    <div class="list-block needs">
      <h2>Needs</h2>
      <p>Belonging - Choice - Clarity - &nbsp;Empathy - Freedom - Meaning<br>Mouring - Peace - Saftey &nbsp;- Understanding<br>&amp; More.....</p>
    </div>
    <div class="list-block feelings">
      <h2>Feelings</h2>
      <p>Confusing - Curious - Despair - Edgy - Fiery - Grief - Nervous<br>Powerless - Shock - Torn - Weary<br>&amp; More....</p>
    </div>
  </section>
</body>
</html>
```